Stylish Business Card for Modern hair salon

I need a simple business card design using our salon logo and colours that are in the logo. We service clients of all ages but predominantly those in the 18 to 55 age range. We have a young staff and are looking to have a card that will present a modern and clean image that represents who we are. The card should be in black and white same as our logo. Minimal use of other colours is allowed.

Industry/Entity Type

Hair And Beauty

Contact Information for Business Card

The design should have the following information
salon name - TR Hair Studio
address - 2751 Birchfield Rd.E. Mississauga, ON L7P3K2
phone - 905 614-2870
website - trhairexample.ca
instagram - tr.hairstudio
twitter - @TR_HairStudio

Colors
000000
ffffff
474747

Requirements
Must have
• simple design, salon name, address, phone, website, instagram, twitter info
• Back of card should have the following:
• YOUR NEXT APPOINTMENT
• DATE
• TIME
Nice to have
• simple design, clear to see and read,
• predominantly black and white colour, minimal use of other colours is ok
Should not have
• many colours, various fonts

```html
<!DOCTYPE html>
<html lang="en">
<head>
<meta charset="utf-8">
<title>TR Hair Studio – Business Card</title>
<link rel="stylesheet" href="https://fonts.googleapis.com/css2?family=Lato:wght@300;400&display=swap">
<style>
  :root {
    --canvas-bg: #2b2b2b;
    --card-bg: #1a1a1a;
    --card-edge: #333333;
    --ink: #ffffff;
    --ink-soft: #d9d9d9;
    --ink-muted: #8a8a8a;
    --rule: #474747;
  }
  * { box-sizing: border-box; margin: 0; padding: 0; }
  html, body {
    width: 1200px; height: 716px; overflow: hidden;
    background: var(--canvas-bg);
    font-family: "Lato", sans-serif;
    color: var(--ink);
  }
  .canvas {
    position: relative; width: 1200px; height: 716px;
    display: flex; align-items: center; justify-content: center; gap: 60px;
  }
  .card {
    position: relative; width: 500px; height: 286px;
    background: var(--card-bg);
    border: 1px solid var(--card-edge);
    border-radius: 20px;
  }
  .brand {
    position: absolute; text-align: center;
    font-weight: 300; color: var(--ink); letter-spacing: 0.06em;
  }
  .brand-name { font-size: 40px; line-height: 1; }
  .brand-rule {
    display: block; height: 1px; background: var(--ink-soft);
    margin: 10px auto 0; width: 100%;
  }
  /* Back: appointment */
  .card-back .brand { left: 0; right: 0; top: 48px; margin: 0 auto; width: 300px; }
  .appointment {
    position: absolute; left: 0; right: 0; top: 150px; text-align: center;
    font-size: 15px; font-weight: 300; color: var(--ink-soft);
  }
  .appointment-fields {
    position: absolute; left: 60px; right: 60px; top: 200px;
    display: flex; justify-content: space-between;
    font-size: 14px; font-weight: 300; color: var(--ink-muted);
  }
  .field { display: flex; align-items: flex-end; gap: 6px; }
  .field-line { display: inline-block; width: 120px; border-bottom: 1px solid var(--ink-muted); height: 14px; }
  /* Front: contact */
  .card-front .brand { left: 40px; top: 36px; width: 300px; }
  .contact-list {
    position: absolute; left: 40px; top: 128px; list-style: none;
    font-size: 14px; font-weight: 300; color: var(--ink-soft);
  }
  .contact-list li { display: flex; align-items: center; gap: 10px; height: 24px; }
  .contact-icon { width: 13px; height: 13px; flex: none; }
  .website {
    position: absolute; right: 24px; bottom: 18px;
    font-size: 13px; font-weight: 300; color: var(--ink-muted);
  }
</style>
</head>
<body>
<main class="canvas">
  <section class="card card-back" aria-label="Card back – appointment">
    <div class="brand">
      <div class="brand-name">TR Hair Studio</div>
      <span class="brand-rule"></span>
    </div>
    <p class="appointment">Your Next Appointment:</p>
    <div class="appointment-fields">
      <span class="field">Date: <span class="field-line"></span></span>
      <span class="field">Time: <span class="field-line"></span></span>
    </div>
  </section>

  <section class="card card-front" aria-label="Card front – contact">
    <div class="brand">
      <div class="brand-name">TR Hair Studio</div>
      <span class="brand-rule"></span>
    </div>
    <ul class="contact-list">
      <li>
        <svg class="contact-icon" viewBox="0 0 12 12" aria-hidden="true"><path d="M6 0.5a4 4 0 0 1 4 4c0 3-4 7-4 7s-4-4-4-7a4 4 0 0 1 4-4z" fill="#d9d9d9"/><circle cx="6" cy="4.5" r="1.5" fill="#1a1a1a"/></svg>
        2751 Birchfield Rd.E. Mississauga, ON L7P3K2
      </li>
      <li>
        <svg class="contact-icon" viewBox="0 0 12 12" aria-hidden="true"><path d="M2.5 1h2l1 2.5-1.3 1a6 6 0 0 0 3.3 3.3l1-1.3 2.5 1v2a1 1 0 0 1-1 1A9.5 9.5 0 0 1 1.5 2a1 1 0 0 1 1-1z" fill="#d9d9d9"/></svg>
        905 614-2870
      </li>
      <li>
        <svg class="contact-icon" viewBox="0 0 12 12" aria-hidden="true"><rect x="1" y="1" width="10" height="10" rx="2" fill="#d9d9d9"/></svg>
        tr.hairstudio
      </li>
      <li>
        <svg class="contact-icon" viewBox="0 0 12 12" aria-hidden="true"><circle cx="6" cy="6" r="5" fill="#d9d9d9"/></svg>
        @TR_HairStudio
      </li>
    </ul>
    <p class="website">trhairexample.ca</p>
  </section>
</main>
</body>
</html>
```